Bref créative
Solo Practice Attorney Biz Cards & Stationery
Biz Cards and Stationery for Solo Practice
Professional
Thomas R. Halvorsen
Attorney At Law
Two Cedar Court
247 N.W. Ninth Street, Suite 2306
Fort Lauderdale, FL 33271
thomas@halvorsenlegalgroup.com
www.halvorsenlegalgroup.com
I would like to see several different ideas for business cards, stationery, and the like. I believe my logo reflects a professional, modern, yet modest character. I would like my other project materials to do the same. I will comment and offer suggestions as the project continues. Many thanks.
Ok, designers: I would like to put a QR Code on the back of the business card that links directly to my website. Does anyone have experience with this? Let me see what you can do.

```html
<!DOCTYPE html>
<html lang="en">
<head>
<meta charset="utf-8">
<title>Halvorsen Legal Group — Business Card</title>
<link href="https://fonts.googleapis.com/css2?family=Marcellus+SC&display=swap" rel="stylesheet">
<style>
  :root {
    --navy: #1d3f7c;
    --navy-deep: #14305f;
    --ink: #2a4a86;
    --text-grey: #4d5560;
    --card-light: #ffffff;
    --card-shade: #d9dcdf;
    --backdrop: #e6e7e9;
  }
  * { margin: 0; padding: 0; box-sizing: border-box; }
  html, body { width: 1200px; height: 901px; overflow: hidden; }
  body {
    background: var(--backdrop);
    font-family: "Marcellus SC", "Times New Roman", serif;
    position: relative;
  }
  .card {
    position: absolute;
    width: 640px;
    height: 366px;
    border-radius: 22px;
    overflow: hidden;
    box-shadow: 0 14px 30px rgba(0,0,0,0.18);
  }

  /* Back side */
  .card-back {
    left: 120px; top: 70px;
    background: linear-gradient(135deg, var(--navy) 0%, var(--navy-deep) 100%);
    color: #fff;
  }
  .back-mark {
    position: absolute;
    left: 0; right: 0; top: 120px;
    text-align: center;
    font-size: 46px;
    letter-spacing: 4px;
    color: #fff;
  }
  .back-web {
    position: absolute;
    left: 0; right: 0; bottom: 34px;
    text-align: center;
    font-size: 15px;
    letter-spacing: 4px;
    color: #e8ecf4;
  }

  /* Front side */
  .card-front {
    left: 440px; top: 460px;
    background: linear-gradient(110deg, var(--card-light) 0%, #f1f2f3 45%, var(--card-shade) 100%);
  }
  .brand {
    position: absolute;
    left: 36px; top: 96px;
    display: flex;
    align-items: flex-start;
    gap: 14px;
  }
  .brand-square {
    width: 40px; height: 40px;
    background: var(--navy);
    margin-top: 6px;
  }
  .brand-name {
    color: var(--navy);
    line-height: 1;
  }
  .brand-name .line-main { display: block; font-size: 34px; letter-spacing: 1px; }
  .brand-name .line-sub { display: block; font-size: 16px; letter-spacing: 1px; margin-top: 8px; }

  .contact {
    position: absolute;
    left: 346px; top: 58px;
    color: var(--text-grey);
    font-size: 13px;
    line-height: 1.35;
  }
  .contact .person { color: var(--ink); font-size: 17px; letter-spacing: 0.5px; }
  .contact .role { font-size: 13px; margin-bottom: 16px; }
  .contact .address { margin-bottom: 16px; }
  .lines { list-style: none; }
  .lines li { display: flex; align-items: center; gap: 8px; height: 19px; }
  .lines svg { width: 13px; height: 13px; fill: var(--text-grey); flex: none; }

  .web-band {
    position: absolute;
    left: 0; bottom: 0;
    width: 640px; height: 48px;
  }
  .web-band-text {
    position: absolute;
    right: 34px; bottom: 14px;
    color: #fff;
    font-size: 15px;
    letter-spacing: 3px;
  }
</style>
</head>
<body>

  <section class="card card-back" aria-label="Business card back">
    <div class="back-mark">Halvorsen</div>
    <div class="back-web">www.halvorsenlegalgroup.com</div>
  </section>

  <section class="card card-front" aria-label="Business card front">
    <div class="brand">
      <div class="brand-square"></div>
      <div class="brand-name">
        <span class="line-main">Halvorsen</span>
        <span class="line-sub">Legal Group, P.A.</span>
      </div>
    </div>

    <div class="contact">
      <div class="person">Thomas R. Halvorsen</div>
      <div class="role">Attorney at Law</div>
      <div class="address">
        Two Cedar Court<br>
        247 N.W. Ninth Street, Suite 2306<br>
        Fort Lauderdale, FL 33271
      </div>
      <ul class="lines">
        <li>
          <svg viewBox="0 0 16 16"><path d="M3 1h3l1.5 4-2 1.3a9 9 0 0 0 4.2 4.2L11 8.5l4 1.5v3a2 2 0 0 1-2 2A12 12 0 0 1 1 3a2 2 0 0 1 2-2z"/></svg>
          (954) 555-0142
        </li>
        <li>
          <svg viewBox="0 0 16 16"><path d="M4 1h8v4H4zM2 6h12a1 1 0 0 1 1 1v5h-3v3H4v-3H1V7a1 1 0 0 1 1-1zm3 6v2h6v-2z"/></svg>
          (850) 555-0187
        </li>
        <li>
          <svg viewBox="0 0 16 16"><path d="M5 0h6a1 1 0 0 1 1 1v14a1 1 0 0 1-1 1H5a1 1 0 0 1-1-1V1a1 1 0 0 1 1-1zm0 2v10h6V2zm3 11a1 1 0 1 0 0 2 1 1 0 0 0 0-2z"/></svg>
          (954) 555-0163
        </li>
        <li>
          <svg viewBox="0 0 16 16"><path d="M1 3h14v10H1zm1.5 1.2V12h11V4.2L8 8.5z M2.8 4 8 7.6 13.2 4z"/></svg>
          thomas@halvorsenlegalgroup.com
        </li>
      </ul>
    </div>

    <svg class="web-band" viewBox="0 0 640 48" preserveAspectRatio="none" aria-hidden="true">
      <polygon points="250,48 275,10 640,10 640,48" fill="#1d3f7c"/>
      <polygon points="0,48 250,48 275,10 282,10 256,48" fill="#14305f" opacity="0"/>
    </svg>
    <div class="web-band-text">www.halvorsenlegalgroup.com</div>
  </section>

</body>
</html>
```